Gin and Spirit labels (4 variations in total from same base)

We need 4 different labels based on the same design, they will differ in color pallete and some text and small design changes.
We need a label elegant and elaborated , ‘classy’, ‘high-end’.
I'm uploading an inspiration folder with photos of labels we like.
Our Brand is "Talvera Spirits", Talvera means moon in Spanish and we would like an elegant design with embossed letters and gold foil.
We are not sure about the material label, we would like an opinion from the designer based on the inspirational photos we are providing.
Our 4 variations are based on our 4 different products:
1) Talvera gin - London Dry gin (black label, golden foil )
2) Talvera Brisa - Cherry Flavoured gin (pink, black , pink or gold foil
3) Talvera Sendero - Cinnamon flavoured spirit (red, orange, black, gold foil)
4) Talvera Vodka (Black, navy blue, silver foil
High end handcraft spirits

```html
<!DOCTYPE html>
<html lang="en">
<head>
<meta charset="utf-8">
<title>Talvera gin – London Dry label</title>
<link rel="stylesheet" href="https://fonts.googleapis.com/css2?family=Rye&family=Great+Vibes&family=Oswald:wght@500&display=swap">
<style>
  :root {
    --backdrop: #d9dbe0;
    --label-black: #060607;
    --label-charcoal: #2b2b2d;
    --gold: #c9a25b;
    --gold-light: #f3dc93;
    --gold-dark: #6e4f22;
    --botanical-grey: #3c3c3f;
    --band-ink: #1c150b;
    --script-cream: #fff4d6;
  }
  html, body {
    margin: 0;
    width: 1200px;
    height: 801px;
    overflow: hidden;
    background: var(--backdrop);
  }
  .canvas {
    position: relative;
    width: 1200px;
    height: 801px;
  }
  .label {
    position: absolute;
    left: 100px;
    top: 80px;
    width: 1000px;
    height: 641px;
    background: linear-gradient(115deg, var(--label-black) 0%, var(--label-charcoal) 50%, var(--label-black) 100%);
    overflow: hidden;
  }
  .botanical-art {
    position: absolute;
    left: 0;
    top: 60px;
    width: 330px;
    height: 581px;
    background: radial-gradient(ellipse at 40% 50%, rgba(60,60,63,0.9) 0%, rgba(60,60,63,0.35) 55%, rgba(60,60,63,0) 80%);
  }
  .botanical-art--top {
    left: 300px;
    top: 0;
    width: 700px;
    height: 150px;
    background: radial-gradient(ellipse at 50% 10%, rgba(60,60,63,0.85) 0%, rgba(60,60,63,0) 75%);
  }
  .emblem {
    position: absolute;
    left: 310px;
    top: 30px;
    width: 380px;
    height: 380px;
  }
  .emblem-ring {
    position: absolute;
    inset: 0;
  }
  .brand-name {
    position: absolute;
    inset: 0;
    margin: 0;
    display: flex;
    flex-direction: column;
    align-items: center;
    justify-content: center;
    font-family: "Rye", serif;
    font-weight: 400;
    color: var(--gold);
    line-height: 1;
  }
  .brand-word {
    font-size: 76px;
    letter-spacing: 1px;
  }
  .brand-kind {
    font-size: 54px;
    margin-top: 8px;
    text-transform: uppercase;
    letter-spacing: 3px;
  }
  .style-name {
    position: absolute;
    left: 0;
    right: 0;
    top: 425px;
    margin: 0;
    text-align: center;
    font-family: "Rye", serif;
    font-weight: 400;
    font-size: 46px;
    letter-spacing: 3px;
    text-transform: uppercase;
    color: var(--gold);
  }
  .foil-band {
    position: absolute;
    left: 0;
    right: 0;
    top: 510px;
    height: 118px;
  }
  .foil-pattern {
    position: absolute;
    inset: 0;
    background: linear-gradient(180deg, var(--gold-dark) 0%, var(--gold) 25%, var(--gold-light) 50%, var(--gold) 75%, var(--gold-dark) 100%);
  }
  .foil-frame {
    position: absolute;
    inset: 0;
  }
  .foil-text {
    position: absolute;
    inset: 0;
    display: flex;
    align-items: center;
    justify-content: space-between;
    padding: 0 34px;
  }
  .volume, .abv {
    font-family: "Oswald", sans-serif;
    font-weight: 500;
    font-size: 20px;
    letter-spacing: 1px;
    color: var(--band-ink);
    width: 140px;
  }
  .abv { text-align: right; }
  .origin-line {
    font-family: "Great Vibes", cursive;
    font-size: 50px;
    color: var(--script-cream);
    text-shadow: 0 1px 2px rgba(40,28,10,0.6);
  }
</style>
</head>
<body>
<main class="canvas">
  <section class="label">
    <div class="botanical-art" role="img" aria-label="Faint grey line drawing of juniper, citrus and gin botanicals"></div>
    <div class="botanical-art botanical-art--top" role="img" aria-label="Faint grey line drawing of juniper sprigs and berries"></div>

    <div class="emblem">
      <svg class="emblem-ring" viewBox="0 0 380 380" aria-hidden="true">
        <circle cx="190" cy="190" r="182" fill="none" stroke="var(--gold)" stroke-width="5"/>
        <circle cx="190" cy="190" r="170" fill="none" stroke="var(--gold)" stroke-width="1.5" stroke-dasharray="60 10 24 8"/>
      </svg>
      <h1 class="brand-name"><span class="brand-word">Talvera</span><span class="brand-kind">gin</span></h1>
    </div>

    <h2 class="style-name">London Dry</h2>

    <div class="foil-band">
      <div class="foil-pattern" role="img" aria-label="Gold foil band with ornate lattice pattern"></div>
      <svg class="foil-frame" viewBox="0 0 1000 118" preserveAspectRatio="none" aria-hidden="true">
        <rect x="8" y="8" width="984" height="102" fill="none" stroke="var(--gold-dark)" stroke-width="2"/>
        <rect x="14" y="14" width="972" height="90" fill="none" stroke="var(--gold-light)" stroke-width="1"/>
      </svg>
      <div class="foil-text">
        <span class="volume">75CL</span>
        <span class="origin-line">Destilado en casa</span>
        <span class="abv">40% ALC VOL</span>
      </div>
    </div>
  </section>
</main>
</body>
</html>
```